Waterproofing specialist needs a flyer design

Our company does repair works for any leakage problems, for example, concrete roofs, balcony, toilets & bathroom, etc. We want our flyers to have a certain focus on the home services that we provide, mainly toilets & bathrooms but not leaving out the rest.

For toilet leakages, we use flood infusion method to water proof and repair toilets. Hence, we like to promote there will be No dust, No noise, No smell, No drilling, No hacking and No removal of existing tile finish. The types of chemical used to manage leakage problems are non-toxic and stops re-bar corrosion. Best of all, it only requires only One-day work. We also provide a call for free consultation.

As we do not have a good picture on waterproofing for illustration, you're welcome to come up with your own pictures that deem fit. The design should communicate reliability and safety.
---------------------------------------------------------

Hi, I have uploaded some of our project pictures for your reference. It is to show an example of what we do in waterproofing. We seal up cracked ceilings or walls basically to prevent water leakage. Understood that the pictures came from TALLFrame, as such, I have also done some research. Searching for "Water damage ceiling" is more relevant our profession. However, I did find more pictures from lenscrate. I have uploaded one example that can be used. Do feedback to me if the uploads helped or more photos are needed to support your design.

Target Market(s)

Households

Industry/Entity Type

Concrete

Requirements
Nice to have
• Pictures

```html
<!DOCTYPE html>
<html lang="en">
<head>
<meta charset="utf-8">
<title>Aquaseal Works Waterproofing Flyer</title>
<link rel="stylesheet" href="https://fonts.googleapis.com/css2?family=Roboto:wght@300;400;500;700&family=Roboto+Condensed:wght@700&display=swap">
<style>
  :root{
    --stage:#1b1b1d;
    --paper:#ffffff;
    --paper-grey:#e4e6e9;
    --navy:#0d3a66;
    --navy-deep:#0a2f55;
    --royal:#1f4fa8;
    --accent:#2b62c4;
    --ink-blue:#2d5d9a;
    --text-light:#e9eef5;
    --text-dark:#333a42;
    --footer:#2f6bb0;
  }
  *{box-sizing:border-box;margin:0;padding:0}
  html,body{width:1200px;height:1000px;overflow:hidden;background:var(--stage);font-family:"Roboto",sans-serif}
  .flyer{position:absolute;left:271px;top:32px;width:659px;height:936px;overflow:hidden;
    background:linear-gradient(180deg,#f2f3f5 0%,var(--paper-grey) 18%,#fbfbfc 20%,var(--paper) 70%,#eef0f3 100%)}
  .flyer svg.shapes{position:absolute;left:0;top:0}
  .brand{position:absolute;left:222px;top:82px;display:flex;align-items:center;gap:14px}
  .brand-dot{width:44px;height:44px;border-radius:50%;background:var(--royal)}
  .brand-name{font-weight:500;font-size:25px;line-height:1.1;color:var(--royal);letter-spacing:.5px}
  .headline{position:absolute;right:30px;top:180px;text-align:right;color:var(--text-light);font-weight:300;line-height:1.25}
  .headline .l1{font-size:24px}
  .headline .l2{font-size:18px}
  .headline .l2 b{font-weight:300;font-size:26px}
  .headline .l3{font-size:30px}
  .services{position:absolute;left:376px;top:314px;list-style:none;color:var(--text-light);font-weight:300;font-size:20px}
  .services li{margin-bottom:15px;position:relative}
  .services li::before{content:"";position:absolute;left:-21px;top:10px;width:7px;height:7px;border-radius:50%;background:var(--text-light)}
  .benefits{position:absolute;right:10px;top:452px;width:340px;text-align:center;color:var(--text-light);font-weight:300;font-size:16px;line-height:22px}
  .photo{position:absolute;border:3px solid #fff;box-shadow:0 2px 4px rgba(0,0,0,.3)}
  .tag{position:absolute;background:var(--navy);color:#fff;font-size:12px;text-align:center;border-radius:7px;line-height:18px}
  .caption{position:absolute;background:var(--navy);color:#fff;font-size:12px;line-height:13px;text-align:center;border-radius:6px;display:flex;align-items:center;justify-content:center;padding:2px 6px}
  .warranty{position:absolute;left:194px;top:620px;width:102px;height:102px;border-radius:50%;background:var(--accent);border:4px solid #fff;box-shadow:0 0 0 3px var(--accent);color:#fff;text-align:center;font-weight:700}
  .warranty .w1{font-size:10px;margin-top:14px}
  .warranty .w2{font-family:"Roboto Condensed",sans-serif;font-size:19px;margin-top:6px;border-top:2px solid #fff;border-bottom:2px solid #fff;padding:2px 0;background:var(--accent)}
  .warranty .w3{font-size:11px;margin-top:3px}
  .cta{position:absolute;left:19px;top:730px}
  .cta .one-day{color:var(--ink-blue);font-size:14px}
  .cta .consult{color:var(--text-dark);font-size:19px;font-weight:300;margin-top:2px}
  .cta .phone{display:flex;align-items:center;gap:10px;margin-top:6px;margin-left:44px;color:var(--navy);font-family:"Roboto Condensed",sans-serif;font-size:37px}
  .note{position:absolute;left:0;right:0;top:852px;text-align:center;color:var(--ink-blue);font-size:17px;font-weight:300;line-height:20px}
  .footer{position:absolute;left:0;right:0;bottom:0;height:34px;background:var(--footer);color:#fff;font-size:15px;font-weight:300;display:flex;align-items:center;padding-left:36px}
  .footer span{display:flex;align-items:center;gap:7px}
  .footer .label{width:203px}
  .footer .tel{width:146px}
</style>
</head>
<body>
<main class="flyer">
  <svg class="shapes" width="659" height="936" viewBox="0 0 659 936">
    <defs>
      <linearGradient id="bandGrad" x1="0" y1="0" x2="0" y2="1">
        <stop offset="0" stop-color="#0f4274"/><stop offset="1" stop-color="#0a2f55"/>
      </linearGradient>
      <linearGradient id="roomGrad" x1="0" y1="0" x2="1" y2="1">
        <stop offset="0" stop-color="#8db4de"/><stop offset=".55" stop-color="#7fa6cf"/><stop offset=".8" stop-color="#8a8c8e"/><stop offset="1" stop-color="#2a211d"/>
      </linearGradient>
    </defs>
    <rect x="230" y="173" width="429" height="417" fill="url(#bandGrad)"/>
    <circle cx="90" cy="376" r="256" fill="var(--accent)"/>
    <circle cx="84" cy="376" r="248" fill="url(#roomGrad)" role="img" aria-label="Photo of a modern blue bathroom with vanity, mirror and freestanding bath"/>
  </svg>

  <div class="brand">
    <div class="brand-dot"></div>
    <div class="brand-name">AQUASEAL WORKS<br>WATERPROOFING</div>
  </div>

  <div class="headline">
    <div class="l1">Specialist in Waterproofing</div>
    <div class="l2">and <b>Repair Works</b> for any</div>
    <div class="l3">leakage problems</div>
  </div>

  <ul class="services">
    <li>Concrete Roofs</li>
    <li>Balcony</li>
    <li>Toilets &amp; Bathroom, Etc.</li>
  </ul>

  <p class="benefits">No Dust, No Noise, No Smell,<br>No Drilling, &nbsp;No Hacking and No Removal<br>of existing tile finish</p>

  <div class="photo" style="left:331px;top:540px;width:114px;height:96px;background:linear-gradient(180deg,#9a5a3c 0%,#b07a55 25%,#c9c5bb 35%,#9d9a92 100%)" role="img" aria-label="Roof ledge before waterproofing"></div>
  <div class="tag" style="left:322px;top:633px;width:129px">Before</div>
  <div class="photo" style="left:508px;top:540px;width:114px;height:96px;background:linear-gradient(180deg,#9a5a3c 0%,#b07a55 25%,#e4e3de 35%,#d2d0ca 100%)" role="img" aria-label="Roof ledge after waterproofing"></div>
  <div class="tag" style="left:499px;top:633px;width:129px">After</div>

  <div class="photo" style="left:331px;top:692px;width:110px;height:86px;background:linear-gradient(180deg,#e8e8e6 0%,#d8d6d0 60%,#b8b2a4 100%)" role="img" aria-label="Toilet with cracked floor tiles"></div>
  <div class="caption" style="left:310px;top:776px;width:154px;height:43px">Water leakage due to cracked floor</div>
  <div class="photo" style="left:508px;top:692px;width:110px;height:86px;background:linear-gradient(180deg,#dcdcda 0%,#eaeae8 60%,#f3f3f1 100%)" role="img" aria-label="Toilet floor being flood infused"></div>
  <div class="caption" style="left:487px;top:776px;width:154px;height:43px">Flood infusion method to water proof and seal the leakage</div>

  <div class="warranty">
    <div class="w1">WITH</div>
    <div class="w2">WARRANTY</div>
    <div class="w3">Provided</div>
  </div>

  <div class="cta">
    <div class="one-day">It requires only ONE-DAY work!</div>
    <div class="consult">CALL FOR FREE CONSULTATION</div>
    <div class="phone">
      <svg width="12" height="22" viewBox="0 0 12 22"><rect x="0.5" y="0.5" width="11" height="21" rx="2" fill="var(--navy)"/><rect x="2.5" y="3" width="7" height="7" fill="#fff"/><g fill="#fff"><rect x="2.5" y="12" width="2" height="2"/><rect x="5" y="12" width="2" height="2"/><rect x="7.5" y="12" width="2" height="2"/><rect x="2.5" y="15" width="2" height="2"/><rect x="5" y="15" width="2" height="2"/><rect x="7.5" y="15" width="2" height="2"/></g></svg>
      9100 4827
    </div>
  </div>

  <p class="note">Types of chemical used to manage leakage problems are non-toxic<br>and stops re-bar corrosion.</p>

  <footer class="footer">
    <span class="label">Office Contact details:</span>
    <span class="tel"><svg width="8" height="12" viewBox="0 0 8 12"><path d="M2 0 L4 0 L4 3 L2.6 3.6 Q2.6 6 4 8.4 L5.4 8 L7 10.6 L5 12 Q0 9 0.6 1 Z" fill="#fff"/></svg>6100 2290</span>
    <span><svg width="12" height="9" viewBox="0 0 12 9"><rect width="12" height="9" fill="#fff"/><path d="M0 0 L6 5 L12 0" stroke="var(--footer)" fill="none"/></svg>info@aquasealworks.com</span>
  </footer>
</main>
</body>
</html>
```